Post Lockdown Ortho Special

We are running a special for (Ortho) Braces/Clear Aligner (Quorventa), till July 31st 2020. Up to $2,000 off with free Consultation and Xrays.

We need a ad to run in different formats.

Maybe something with: what better time to get braces when you have to wear a mask all the time.

Trying to rebuild our business and get people in for free consultations.

```html
<!DOCTYPE html>
<html lang="en">
<head>
<meta charset="utf-8">
<title>Post Lockdown Ortho Special</title>
<link href="https://fonts.googleapis.com/css2?family=Cinzel:wght@400;700&family=Roboto:wght@400;500;700&family=Roboto+Condensed:wght@700&display=swap" rel="stylesheet">
<style>
  :root {
    --page: #f2f2f2;
    --purple: #6d47a8;
    --purple-light: #8f70c2;
    --purple-deep: #5b3996;
    --cream: #fce9dd;
    --rule: #6e6e6e;
    --ink: #222222;
    --white: #ffffff;
  }
  * { box-sizing: border-box; margin: 0; padding: 0; }
  html, body { width: 1200px; height: 1200px; overflow: hidden; background: var(--page); }
  .ad {
    position: absolute; left: 50px; top: 211px;
    width: 1100px; height: 777px;
    background: var(--white); overflow: hidden;
    font-family: "Roboto", Arial, sans-serif; color: var(--ink);
  }
  .hero-band {
    position: absolute; left: 0; top: 0; width: 1100px; height: 538px;
    background: linear-gradient(180deg, var(--purple-deep) 0%, var(--purple) 45%, var(--purple-light) 75%, var(--purple) 100%);
  }
  .hero-photo {
    position: absolute; right: 0; top: 0; width: 505px; height: 538px;
    background: linear-gradient(90deg, rgba(143,112,194,0) 0%, #c9a7a4 30%, #e6c3b2 55%, #d8b6a8 75%, #9a7cc4 100%);
  }
  .rule {
    position: absolute; left: 0; top: 545px; width: 1100px; height: 7px; background: var(--rule);
  }
  .headline { position: absolute; left: 60px; top: 50px; font-family: "Cinzel", Georgia, serif; color: var(--white); line-height: 1; }
  .headline span { display: block; }
  .headline .small { font-size: 25px; font-weight: 400; }
  .headline .huge { font-size: 68px; font-weight: 700; margin-top: 8px; }
  .headline .mid { font-size: 35px; font-weight: 400; margin-top: 12px; }
  .headline .big { font-size: 54px; font-weight: 700; margin-top: 10px; }
  .headline .large { font-size: 42px; font-weight: 700; margin-top: 10px; }
  .offer-note {
    position: absolute; left: 54px; top: 344px; width: 549px; height: 85px;
    background: var(--cream); border-radius: 20px;
    padding: 14px 0 0 26px; font-size: 20px; line-height: 27px;
  }
  .offer-note b { font-weight: 500; }
  .smile-tile {
    position: absolute; top: 457px; width: 230px; height: 154px; border-radius: 16px;
    background: radial-gradient(ellipse at 50% 50%, #f4f0ee 0%, #f4f0ee 25%, #d97c86 45%, #efc7c3 75%, #f3d8cc 100%);
  }
  .smile-tile.braces { left: 64px; }
  .smile-tile.aligner { left: 321px; }
  .discount-badge {
    position: absolute; left: 720px; top: 372px; width: 252px; height: 252px; border-radius: 50%;
    background: var(--cream); box-shadow: 0 10px 14px -8px rgba(0,0,0,.35);
  }
  .discount-badge::before {
    content: ""; position: absolute; inset: 6px; border-radius: 50%;
    border: 2px dotted #777;
  }
  .badge-text { position: absolute; left: 0; top: 44px; width: 100%; text-align: center; }
  .badge-text .upto { font-size: 20px; }
  .badge-text .amount { font-family: "Roboto Condensed", Arial, sans-serif; font-weight: 700; font-size: 66px; line-height: 64px; color: #2b2b2b; }
  .badge-text .off {
    display: flex; align-items: center; justify-content: center; gap: 6px;
    font-size: 18px; line-height: 18px; margin: 2px auto 0; width: 164px;
  }
  .badge-text .off::before, .badge-text .off::after { content: ""; flex: 1; height: 1px; background: #333; }
  .badge-text .terms { font-size: 15px; line-height: 20px; margin-top: 2px; }
  .badge-text .terms b { font-weight: 500; }
  .badge-text .underline { width: 164px; height: 1px; background: #333; margin: 6px auto 0; }
  .practice { position: absolute; left: 100px; top: 650px; display: flex; align-items: center; gap: 14px; }
  .practice-mark { width: 60px; height: 60px; border-radius: 50%; background: var(--purple); flex: none; }
  .practice-name { font-family: "Cinzel", Georgia, serif; font-weight: 700; color: var(--purple); font-size: 20px; line-height: 24px; width: 230px; }
  .practice-doctor { font-family: "Cinzel", Georgia, serif; font-size: 10px; color: #777; letter-spacing: 1px; margin-top: 4px; font-weight: 400; }
  .divider { position: absolute; left: 437px; top: 638px; width: 1px; height: 94px; background: #555; }
  .call-bar {
    position: absolute; left: 479px; top: 636px; width: 546px; height: 53px;
    background: var(--purple); display: flex; align-items: center; padding: 3px;
  }
  .call-label { width: 253px; color: var(--white); font-size: 27px; text-align: center; }
  .call-number { flex: 1; height: 100%; background: var(--cream); font-size: 31px; font-weight: 500; display: flex; align-items: center; justify-content: center; }
  .contact { position: absolute; top: 703px; display: flex; align-items: center; gap: 8px; font-size: 17px; }
  .contact.email { left: 484px; }
  .contact.web { left: 782px; }
  .contact-icon { width: 34px; height: 34px; border-radius: 50%; background: var(--purple); display: flex; align-items: center; justify-content: center; }
</style>
</head>
<body>
  <main class="ad">
    <div class="hero-band" role="img" aria-label="Purple-tinted lakeside pine forest and mountain landscape"></div>
    <div class="hero-photo" role="img" aria-label="Smiling woman holding a clear aligner"></div>
    <div class="rule"></div>

    <h1 class="headline">
      <span class="small">What better time to</span>
      <span class="huge">GET BRACES</span>
      <span class="mid">WHEN YOU HAVE&nbsp; TO</span>
      <span class="big">WEAR A MASK</span>
      <span class="large">ALL THE TIME</span>
    </h1>

    <p class="offer-note">We are running a <b>special for (Ortho) Braces/Clear Aligner (Quorventa)</b>, till <b>July 31st 2020</b></p>

    <div class="smile-tile braces" role="img" aria-label="Close-up of a smile with metal braces"></div>
    <div class="smile-tile aligner" role="img" aria-label="Smile shown half with braces, half straightened"></div>

    <div class="discount-badge">
      <div class="badge-text">
        <div class="upto">Up to</div>
        <div class="amount">$2,000</div>
        <div class="off">OFF</div>
        <div class="terms">with <b>free Consultation</b><br>and <b>Xrays</b></div>
        <div class="underline"></div>
      </div>
    </div>

    <div class="practice">
      <div class="practice-mark"></div>
      <div class="practice-name">Pinecrest Family Dentistry
        <div class="practice-doctor">DR ELENA MARSH</div>
      </div>
    </div>
    <div class="divider"></div>

    <div class="call-bar">
      <span class="call-label">CALL US NOW</span>
      <span class="call-number">555-204-3817</span>
    </div>

    <div class="contact email">
      <span class="contact-icon">
        <svg width="18" height="14" viewBox="0 0 18 14" fill="none" stroke="#fff" stroke-width="1.6"><rect x="1" y="1" width="16" height="12" rx="1"/><path d="M1 1l8 7 8-7M1 13l6-6M17 13l-6-6"/></svg>
      </span>
      hello@pinecrestsmiles.com
    </div>
    <div class="contact web">
      <span class="contact-icon">
        <svg width="16" height="20" viewBox="0 0 16 20"><path d="M8 1a6.5 6.5 0 0 0-6.5 6.5C1.5 12 8 19 8 19s6.5-7 6.5-11.5A6.5 6.5 0 0 0 8 1z" fill="#fff"/><circle cx="8" cy="7.5" r="2.5" fill="#6d47a8"/></svg>
      </span>
      www.pinecrestsmiles.com
    </div>
  </main>
</body>
</html>
```